Bicycle Tour Schedule on a Business Card

Need to develop a 2 side business card that highlights a series of bike tours on 1 side and a series of events on the other side.
This will be inserted into a card wallet that attaches to a cell phone and will be handed out at an expo. The card wallets are black and red so color must coordinate with both. There is a photo of the card wallets attached.

1 side needs to be devoted to Pedal Vista Rides and the others to KRV Outcome events on the other. Dates and websites are very important.

Target Market(s)

Cyclists
Predominantly men ages 40+
Educated, Professionals

Industry/Entity Type

Business

Font styles to use
Serif

Requirements
Must have
• Pedal vista rides logo on 1 side and KRV Outcome logo on the other side
• dates and websites clearly visible
• Design of both sides must go together.
• Must be portrait not landscape

```html
<!DOCTYPE html>
<html lang="en">
<head>
<meta charset="utf-8">
<title>Pedal Vista Rides – Tour Schedule Card</title>
<link href="https://fonts.googleapis.com/css2?family=Merriweather:wght@700&family=Oranienbaum&family=PT+Sans:wght@400;700&display=swap" rel="stylesheet">
<style>
  :root {
    --page: #ffffff;
    --card: #433f3e;
    --white: #ffffff;
    --brand-green: #4cb56a;
    --bullet-green: #3fd81a;
    --url-green: #1c7a1c;
    --wedge-bright: #44f011;
    --wedge-mid: #2f9c18;
    --wedge-dark: #1d5c10;
    --accent-red: #d0152c;
  }
  * { margin: 0; padding: 0; box-sizing: border-box; }
  html, body { width: 1200px; height: 1000px; overflow: hidden; background: var(--page); }
  .canvas { position: relative; width: 1200px; height: 1000px; }

  .card {
    position: absolute; top: 70px; width: 429px; height: 867px;
    background: var(--card); overflow: hidden; color: var(--white);
  }
  .card--tours { left: 122px; }
  .card--events { left: 655px; width: 430px; font-family: "PT Sans", sans-serif; }

  /* Tours side */
  .brand-name {
    position: absolute; top: 170px; left: 0; width: 100%;
    display: flex; align-items: center; justify-content: center; gap: 14px;
    font-family: "PT Sans", sans-serif; font-weight: 700; font-size: 46px;
    color: var(--brand-green);
  }
  .brand-name .mark { width: 22px; height: 22px; border-radius: 50%; background: var(--brand-green); }
  .tagline {
    position: absolute; top: 330px; left: 0; width: 100%; text-align: center;
    font-family: "Merriweather", serif; font-weight: 700; font-size: 20px; line-height: 31px;
  }
  .tour-list { position: absolute; top: 462px; left: 24px; list-style: none; font-family: "Oranienbaum", serif; font-size: 27px; }
  .tour { position: relative; height: 43px; }
  .condensed { display: inline-block; transform-origin: left center; white-space: nowrap; }
  .tour-name { position: absolute; left: 17px; top: 0; }
  .tour-name .condensed { transform: scaleX(0.58); font-weight: 700; }
  .tour-name::before {
    content: ""; position: absolute; left: -11px; top: 11px; width: 12px; height: 12px;
    border-radius: 50%; background: radial-gradient(circle at 35% 35%, #b6ff8a, var(--bullet-green) 60%, #1f8a10);
  }
  .tour-date { position: absolute; left: 220px; top: 0; line-height: 41px; margin-top: -6px; }
  .tour-date .condensed { transform: scaleX(0.62); }
  .tour-date::before {
    content: ""; position: absolute; left: -28px; top: 11px;
    border-left: 20px solid var(--bullet-green); border-top: 9px solid transparent; border-bottom: 9px solid transparent;
  }
  .wedge { position: absolute; left: 0; bottom: 0; }

  /* Events side */
  .series-title { position: absolute; top: 68px; left: 0; width: 100%; text-align: center; font-weight: 700; font-size: 23px; }
  .event { position: absolute; left: 20px; width: 400px; font-size: 17px; line-height: 26px; }
  .event-name { position: relative; padding-left: 9px; }
  .event-name::before {
    content: ""; position: absolute; left: 0; top: 10px; width: 6px; height: 6px;
    border-radius: 50%; background: var(--bullet-green);
  }
  .event-date { position: absolute; left: 236px; top: 0; padding-left: 16px; white-space: nowrap; }
  .event-date--low { top: 26px; }
  .event-date::before {
    content: ""; position: absolute; left: 0; top: 8px;
    border-left: 10px solid var(--bullet-green); border-top: 5px solid transparent; border-bottom: 5px solid transparent;
  }
  .event-url {
    display: inline-block; margin-left: 6px; margin-top: 2px; padding: 0 4px;
    background: var(--url-green); font-size: 19px; line-height: 26px;
  }
  .event--camps { top: 163px; }
  .event--century { top: 291px; }
  .event--park { top: 403px; }
  .event--zany { top: 549px; }

  .footer-rule { position: absolute; left: 0; right: 0; top: 833px; height: 3px; background: var(--accent-red); }
  .footer-brand {
    position: absolute; right: 30px; top: 796px;
    display: flex; align-items: center; gap: 8px;
    font-weight: 700; font-size: 24px; color: var(--accent-red);
  }
  .footer-brand .mark { width: 12px; height: 12px; background: var(--accent-red); }
</style>
</head>
<body>
<main class="canvas">
  <section class="card card--tours">
    <div class="brand-name"><span class="mark"></span>Pedal Vista Rides</div>
    <p class="tagline">Fully supported bike tours.<br>Discover the hidden gems on two wheels.</p>
    <ul class="tour-list">
      <li class="tour"><span class="tour-name"><span class="condensed">Heart of Colorado</span></span><span class="tour-date"><span class="condensed">June 26 – July 2, 2016</span></span></li>
      <li class="tour"><span class="tour-name"><span class="condensed">Colorado Front Range Tour</span></span><span class="tour-date"><span class="condensed">August14-20, 2016</span></span></li>
      <li class="tour"><span class="tour-name"><span class="condensed">Cape Cod Tour</span></span><span class="tour-date"><span class="condensed">October 9 -15, 2016</span></span></li>
      <li class="tour"><span class="tour-name"><span class="condensed">Florida Key Tours</span></span><span class="tour-date"><span class="condensed">November 6-12, 2016 &amp;<br>December 4-10, 2016</span></span></li>
    </ul>
    <svg class="wedge" width="429" height="160" viewBox="0 0 429 160" aria-hidden="true">
      <polygon points="0,160 429,0 429,160" fill="var(--wedge-bright)"/>
      <polygon points="0,160 429,45 429,160" fill="var(--wedge-mid)"/>
      <polygon points="0,160 429,95 429,160" fill="var(--wedge-dark)"/>
    </svg>
  </section>

  <section class="card card--events">
    <h1 class="series-title">Tri Spoke Series:&nbsp; Cycling camps for youth</h1>

    <div class="event event--camps">
      <div class="event-name">Mountain Bike Camp<span class="event-date">July 8-10, 2016</span></div>
      <div class="event-name">Cyclocross Camp<span class="event-date">August 26-28, 2016</span></div>
      <span class="event-url">Trispokeseries.org</span>
    </div>

    <div class="event event--century">
      <div class="event-name">Summit Century Ride<span class="event-date">June 18, 2016</span></div>
      <span class="event-url">Summitcenturyride.com</span>
    </div>

    <div class="event event--park">
      <div class="event-name">Ridgeline Park 2<br>Park Challenge<span class="event-date event-date--low">July 30, 2016</span></div>
      <span class="event-url">Ridgepark2park.com</span>
    </div>

    <div class="event event--zany">
      <div class="event-name">Zany Wheel Ride<span class="event-date">September 11, 2016</span></div>
      <span class="event-url">zanywheelride.com</span>
    </div>

    <div class="footer-rule"></div>
    <div class="footer-brand"><span class="mark"></span>KRV Outcome</div>
  </section>
</main>
</body>
</html>
```